KTR Vials

Sales Sheet (2-Sided) 8 1/2 x 11 Size
Company Sells Prescription Vials and Toner to Pharmacies

Sales Sheet
Side ONE (FRONT)
Graphic: KTR Services Logo Text: Quality Vials without the Premium Price
Primary Message: Busy Schedule? (Photo of Male or Female Pharmacist)
Secondary Message: Let Us Make Ordering Pharmacy Vials Easy For You!
EASY and CONVENIENT
ORDER ONLINE ktrservices.example
ORDER BY PHONE 888-413-5276
ORDER BY FAX 855-307-4182
KTR Services’ line of pharmacy vials, bottles and jars brings you the highest quality products at the lowest prices.
Graphic Element or Call Out: High quality, low prices, great customer service, free shipping (over $90) and a vast inventory selection
Vials

Jars and Liquid

Can’t find a particular product? Call Us and we will do everything to get the product for you. We want to be your source for pharmacy vials and toner supplies.
To place an order, or receive additional information and pricing please contact our customer service representatives at customer@ktrservices.example, online chat at ktrservices.example or 888-413-5276.

Back Side:
Graphic Element Needed: The more you need, the more you save.
The more you buy, earn higher discounts. You receive a 5% discount on every three cases purchased, up to 12% discount.
Mix and match quantities include all vials, bottles and jars, all type caps!
Everyday Quantity Discounts (Mix and Match Your Order)
(Graphic Element or call outs for below)
5% for every three (3) cases
8% for every six (6) cases
12% for every eleven (11) plus cases
Graphic Element Needed - Gift Card or KTR Store Credit for Your Referrals
KTR Services knows the importance of our customers. We know that if you have a great experience with us, and refer us to another customer, we want to reward you for your referrals. For every customer you refer to us that makes a purchase. The more you refer, the more you can earn. Call us today at 888-413-5276.
You can view our line of pharmacy vials and ink & toner products on www.ktrservices.example.

ORDER BY FAX 855-307-4182

Please call 888-413-5276 for Vial Samples, Vials and Toner Bundle Pricing & Additional Information.

Industry/Entity Type

It Company

Requirements
Must have
• Use Logo Attached
Should not have
• clipart illustrations of dollar bills

```html
<!DOCTYPE html>
<html lang="en">
<head>
<meta charset="utf-8">
<title>KTR Services – Sales Sheet</title>
<link rel="stylesheet" href="https://fonts.googleapis.com/css2?family=Arimo:wght@700&family=Arvo:wght@700&family=Cinzel:wght@600&family=Open+Sans:ital,wght@1,700&family=Questrial&family=Roboto+Condensed:wght@700&family=Titillium+Web:wght@400;700&display=swap">
<style>
  :root {
    --blue: #1a86c4;
    --blue-deep: #156ea8;
    --navy: #2b2c8a;
    --headline-blue: #2b74c0;
    --green: #7cc242;
    --green-deep: #0f8a3a;
    --green-text: #148d3c;
    --ink: #2d3a3a;
    --steel: #5e7c93;
    --paper: #fbfcf9;
    --paper-tint: #e9f2e1;
  }
  * { box-sizing: border-box; margin: 0; padding: 0; }
  html, body { width: 936px; height: 1200px; overflow: hidden; }
  body { background: #ffffff; }
  .sheet {
    position: relative; width: 936px; height: 1200px; overflow: hidden;
    background: radial-gradient(ellipse at 30% 35%, var(--paper) 40%, var(--paper-tint) 100%);
  }
  .abs { position: absolute; }
  .brand { left: 50px; top: 70px; display: flex; align-items: center; gap: 10px; }
  .brand-dot { width: 26px; height: 26px; border-radius: 50%; background: var(--green); }
  .brand-name {
    font-family: "Roboto Condensed", sans-serif; font-weight: 700;
    font-size: 25px; color: var(--navy); letter-spacing: 0.2px;
  }
  .tagline-band { left: 0; top: 0; }
  .tagline {
    left: 282px; top: 112px; width: 640px;
    font-family: "Cinzel", serif; font-weight: 600; font-size: 23px; color: #fff;
    letter-spacing: 0.6px; white-space: nowrap;
  }
  .headline {
    left: 58px; top: 298px; font-family: "Arimo", sans-serif; font-weight: 700;
    font-size: 44px; line-height: 51px; color: var(--headline-blue);
  }
  .subhead {
    left: 59px; top: 420px; font-family: "Arimo", sans-serif; font-weight: 700;
    font-size: 20px; line-height: 26px; color: var(--navy);
  }
  .pharmacist-photo {
    left: 342px; top: 190px; width: 594px; height: 337px;
    background: linear-gradient(90deg, #dfe3e6 0%, #eceeef 45%, #f1ebe4 70%, #e8e3dc 100%);
  }
  .easy-band { left: 0; top: 541px; }
  .easy-label {
    left: 237px; top: 548px; width: 520px; text-align: center;
    font-family: "Titillium Web", sans-serif; font-weight: 700; font-size: 24px; color: #fff;
  }
  .order-list {
    left: 59px; top: 617px; font-family: "Titillium Web", sans-serif;
    font-size: 23px; line-height: 29px; color: var(--green-deep);
    display: grid; grid-template-columns: 211px auto;
  }
  .order-list .value { font-weight: 700; }
  .promise {
    left: 492px; top: 612px; width: 370px; text-align: center;
    font-family: "Open Sans", sans-serif; font-style: italic; font-weight: 700;
    font-size: 20.5px; line-height: 29px; color: var(--navy);
  }
  .callout-band { left: 0; top: 746px; }
  .callout {
    left: 60px; top: 765px; width: 816px; text-align: center;
    font-family: "Roboto Condensed", sans-serif; font-weight: 700;
    font-size: 31px; line-height: 42px; color: #fff;
  }
  .section-title {
    left: 39px; top: 940px; font-family: "Arvo", serif; font-weight: 700;
    font-size: 29px; color: var(--green-text);
  }
  .body-copy {
    left: 39px; width: 860px; font-family: "Questrial", sans-serif;
    font-size: 19.5px; line-height: 27px; color: var(--ink); letter-spacing: 0.3px;
  }
  .body-copy strong { font-weight: 700; color: #111; font-family: "Arimo", sans-serif; }
  .body-copy.first { top: 996px; }
  .body-copy.second { top: 1064px; }
  .foot-band { left: 0; top: 1174px; }
</style>
</head>
<body>
<main class="sheet">
  <div class="abs brand">
    <span class="brand-dot"></span>
    <span class="brand-name">KTR Services, LLC.</span>
  </div>

  <svg class="abs tagline-band" width="936" height="185" viewBox="0 0 936 185" aria-hidden="true">
    <polygon points="602,86 936,86 936,96 596,96" fill="var(--green)"/>
    <polygon points="237,104 936,104 936,160 262,160" fill="var(--blue)"/>
    <polygon points="277,164 520,164 514,176 283,176" fill="var(--green)"/>
  </svg>
  <p class="abs tagline">Quality Vials without the Premium Price</p>

  <h1 class="abs headline">Busy<br>Schedule?</h1>
  <p class="abs subhead">Let Us Make Ordering<br>Pharmacy Vials Easy<br>For You!</p>

  <div class="abs pharmacist-photo" role="img" aria-label="Photo of a smiling pharmacist in a white coat in front of pharmacy shelves"></div>

  <svg class="abs easy-band" width="936" height="42" viewBox="0 0 936 42" aria-hidden="true">
    <defs>
      <linearGradient id="g-left" x1="0" x2="1"><stop offset="0" stop-color="#a6d46a"/><stop offset="1" stop-color="#5fb53e"/></linearGradient>
      <linearGradient id="g-right" x1="0" x2="1"><stop offset="0" stop-color="#5fb53e"/><stop offset="1" stop-color="#a6d46a"/></linearGradient>
    </defs>
    <polygon points="0,0 205,0 230,42 0,42" fill="url(#g-left)"/>
    <polygon points="238,0 780,0 763,42 258,42" fill="var(--blue-deep)"/>
    <polygon points="790,0 936,0 936,42 772,42" fill="url(#g-right)"/>
  </svg>
  <p class="abs easy-label">EASY and CONVENIENT</p>

  <div class="abs order-list">
    <span>ORDER ONLINE</span><span class="value">ktrservices.example</span>
    <span>ORDER BY PHONE</span><span class="value">888-413-5276</span>
    <span>ORDER BY FAX</span><span class="value">855-307-4182</span>
  </div>
  <p class="abs promise">KTR Services’ line of pharmacy vials, bottles and jars brings you the highest quality products at the lowest prices.</p>

  <svg class="abs callout-band" width="936" height="172" viewBox="0 0 936 172" aria-hidden="true">
    <defs>
      <linearGradient id="steel-l" x1="0" x2="1"><stop offset="0" stop-color="var(--steel)"/><stop offset="1" stop-color="#c3ccd3"/></linearGradient>
      <linearGradient id="steel-r" x1="0" x2="1"><stop offset="0" stop-color="#c3ccd3"/><stop offset="1" stop-color="var(--steel)"/></linearGradient>
      <radialGradient id="green-c" cx="0.5" cy="0.9" r="0.7"><stop offset="0" stop-color="#3fbf4a"/><stop offset="1" stop-color="var(--green-deep)"/></radialGradient>
    </defs>
    <polygon points="0,0 44,0 126,172 0,172" fill="url(#steel-l)"/>
    <polygon points="900,0 936,0 936,172 850,172" fill="url(#steel-r)"/>
    <polygon points="50,0 892,0 842,172 132,172" fill="url(#green-c)"/>
  </svg>
  <p class="abs callout">High quality, low prices,<br>great customer service, free shipping (over $90)<br>and a vast inventory selection Vials</p>

  <h2 class="abs section-title">Jars and Liquid</h2>
  <p class="abs body-copy first">Can’t find a particular product? Call Us and we will do everything to get the product for you. We want to be your source for pharmacy vials and toner supplies.</p>
  <p class="abs body-copy second">To place an order, or receive additional information and pricing please contact our customer service representatives at <strong>customer@ktrservices.example</strong>, online chat at <strong>ktrservices.example</strong> or <strong>888-413-5276</strong>.</p>

  <svg class="abs foot-band" width="936" height="26" viewBox="0 0 936 26" aria-hidden="true">
    <polygon points="0,0 270,0 282,26 0,26" fill="var(--blue)"/>
    <polygon points="278,0 936,0 936,26 290,26" fill="var(--green)"/>
  </svg>
</main>
</body>
</html>
```